Postcard flyer for body postive dance classes

We need an eye catching double sided A6 postcard for body positive dance classes. The business name is stepbloomjoy and already have a rough logo and some text that needs tidying up and putting together. The design needs to be simple and elegant. We are appealing to a diverse range of adult women with or without dance experience to join us in a safe, supportive and creative environment. We would like the design to use black, white and a soft green. The final design should communicate movement, contentment and wholeness. File with information attached.

Target Market(s)

Diverse range of adult women

Industry/Entity Type

Health And Wellness

Font styles to use
Other font styles liked:
• Candara or similar but open to suggestions

Colors
abd036
cadf82
eaf2ce
fffefb
fef9ed
fff3d1
ffffff

Requirements
Must have
• Logo and text provided.
Nice to have
• Sense of movement. Match to website colours and style.
Should not have
• Intimidating perfect body images

```html
<!DOCTYPE html>
<html lang="en">
<head>
<meta charset="utf-8">
<title>stepbloomjoy – postcard</title>
<link href="https://fonts.googleapis.com/css2?family=Source+Sans+3:ital,wght@0,400;0,600;0,700;1,400&display=swap" rel="stylesheet">
<style>
  :root {
    --page: #ecebe8;
    --white: #ffffff;
    --green: #abd036;
    --green-soft: #cadf82;
    --green-pale: #eaf2ce;
    --grey-panel: #d4d4d6;
    --grey-light: #f1f1f1;
    --ink: #3d3d3d;
    --ink-soft: #5a5a5a;
    --rule: #9a9a9a;
  }
  * { box-sizing: border-box; margin: 0; padding: 0; }
  html, body { width: 896px; height: 1200px; overflow: hidden; }
  body {
    background: var(--page);
    font-family: "Source Sans 3", sans-serif;
    color: var(--ink);
    position: relative;
  }
  .postcard {
    position: absolute;
    left: 118px;
    width: 661px;
    height: 471px;
    background: var(--white);
    overflow: hidden;
    box-shadow: 0 2px 8px rgba(0,0,0,.18);
  }
  .postcard--front { top: 85px; }
  .postcard--back { top: 598px; }

  /* front */
  .front-panel { position: absolute; left: 0; width: 440px; }
  .front-panel--intro { top: 0; height: 196px; background: var(--white); }
  .front-panel--invite { top: 196px; height: 148px; background: var(--green-pale); }
  .front-panel--closing { top: 344px; height: 127px; background: var(--grey-panel); }
  .accent-strip {
    position: absolute; inset: 0;
    background: var(--green-soft);
    clip-path: polygon(342px 0, 372px 0, 302px 471px, 272px 471px);
  }
  .photo {
    position: absolute; inset: 0;
    background: radial-gradient(ellipse at 60% 35%, #e8e8e8 0%, #b5b5b5 45%, #6d6d6d 100%);
    clip-path: polygon(372px 0, 661px 0, 661px 471px, 302px 471px);
  }
  .headline { position: absolute; left: 28px; top: 44px; font-size: 24px; font-weight: 400; white-space: nowrap; }
  .headline em { font-style: normal; color: var(--green); }
  .intro-copy, .invite-copy, .closing-copy {
    position: absolute; left: 28px; font-size: 18px; line-height: 22px; color: var(--ink-soft); white-space: nowrap;
  }
  .intro-copy { top: 94px; }
  .invite-copy { top: 211px; color: var(--ink); }
  .invite-copy strong { font-weight: 700; }
  .closing-copy { top: 355px; color: var(--ink); }
  .front-url { position: absolute; left: 28px; top: 423px; font-size: 17px; font-weight: 700; }
  .ribbon {
    position: absolute; right: -46px; top: 30px;
    width: 240px; height: 30px;
    background: var(--green-pale);
    transform: rotate(35deg);
    display: flex; align-items: center; justify-content: center;
    font-size: 11px; letter-spacing: .5px; color: var(--ink);
  }
  .brand-badge {
    position: absolute; left: 254px; top: 324px;
    width: 118px; height: 118px; border-radius: 50%;
    background: var(--white);
    box-shadow: 0 2px 6px rgba(0,0,0,.25);
    display: flex; align-items: center; justify-content: center;
    font-size: 15px; font-weight: 600; color: var(--ink-soft);
  }

  /* back */
  .back-shade {
    position: absolute; inset: 0;
    background: var(--grey-light);
    clip-path: polygon(101px 0, 389px 0, 389px 426px, 17px 426px);
  }
  .divider { position: absolute; left: 389px; top: 0; width: 1px; height: 471px; background: #e6e6e6; }
  .back-name { position: absolute; left: 0; width: 389px; top: 66px; text-align: center; font-size: 32px; letter-spacing: .5px; color: var(--ink-soft); }
  .back-motto {
    position: absolute; left: 0; width: 389px; top: 137px; height: 43px;
    background: var(--green-pale);
    text-align: center; font-size: 17px; line-height: 19px; padding-top: 3px; color: var(--ink);
  }
  .back-mark {
    position: absolute; left: 100px; top: 250px; width: 190px;
    display: flex; align-items: center; justify-content: center; gap: 10px;
    font-size: 20px; color: #8c8c8c;
  }
  .back-mark .dot { width: 24px; height: 24px; border: 2px solid #8c8c8c; border-radius: 50%; }
  .values { position: absolute; left: 0; width: 389px; top: 352px; text-align: center; font-size: 15.5px; font-style: italic; color: var(--ink-soft); }
  .contact-row { position: absolute; left: 28px; top: 396px; display: flex; gap: 16px; font-size: 16px; align-items: center; white-space: nowrap; }
  .contact-row span { display: flex; align-items: center; gap: 7px; }
  .contact-row svg { width: 17px; height: 17px; }
  .back-url {
    position: absolute; left: 0; top: 426px; width: 389px; height: 45px;
    background: var(--green);
    text-align: center; line-height: 45px; font-size: 21px; letter-spacing: .3px; color: var(--ink);
  }
  .mail-contact { position: absolute; left: 395px; top: 22px; font-size: 9.5px; line-height: 1.25; font-weight: 600; color: var(--ink); }
  .stamp-box { position: absolute; left: 555px; top: 22px; width: 85px; height: 61px; border: 1px solid var(--rule); }
  .address-line { position: absolute; left: 413px; width: 225px; height: 1px; background: var(--rule); }
</style>
</head>
<body>
  <section class="postcard postcard--front">
    <div class="front-panel front-panel--intro"></div>
    <div class="front-panel front-panel--invite"></div>
    <div class="front-panel front-panel--closing"></div>
    <div class="accent-strip"></div>
    <div class="photo" role="img" aria-label="Black and white photo of a smiling woman dancing with her arms raised"></div>
    <h1 class="headline">Dance is <em>JOY,</em> dance is <em>LOVE.</em></h1>
    <p class="intro-copy">Dance is at the core of our being,<br>a celebration of movement,<br>vitality and wholeness.</p>
    <p class="invite-copy">If you’ve never danced before and<br>always wanted to or you want to<br>reignite your past love of dance,<br>join us at <strong>stepbloomjoy</strong> to start<br>your journey.</p>
    <p class="closing-copy">Flow with life through your<br>inner dancer.</p>
    <p class="front-url">www.stepbloomjoy.com.au</p>
    <div class="ribbon">NEW DANCE CLASSES</div>
    <div class="brand-badge">stepbloomjoy</div>
  </section>

  <section class="postcard postcard--back">
    <div class="back-shade"></div>
    <div class="divider"></div>
    <p class="back-name">stepbloomjoy</p>
    <p class="back-motto">FLOW WITH LIFE THROUGH YOUR<br>INNER DANCER.</p>
    <div class="back-mark"><span class="dot"></span>stepbloomjoy</div>
    <p class="values">movement, contentment, wholeness</p>
    <div class="contact-row">
      <span>
        <svg viewBox="0 0 16 16" aria-hidden="true"><circle cx="8" cy="8" r="7" fill="none" stroke="#3d3d3d" stroke-width="1.2"/><path d="M5.3 4.6l1.3-.4.8 1.8-.9.7c.4.9 1.1 1.6 2 2l.7-.9 1.8.8-.4 1.3c-2.8.2-5.5-2.5-5.3-5.3z" fill="#3d3d3d"/></svg>
        0400518276
      </span>
      <span>
        <svg viewBox="0 0 16 16" aria-hidden="true"><circle cx="8" cy="8" r="7" fill="none" stroke="#3d3d3d" stroke-width="1.2"/><rect x="7.3" y="7" width="1.4" height="4.5" fill="#3d3d3d"/><circle cx="8" cy="5" r=".9" fill="#3d3d3d"/></svg>
        hello@stepbloomjoy.com.au
      </span>
    </div>
    <p class="back-url">www.stepbloomjoy.com.au</p>
    <p class="mail-contact">Contact<br>E: hello@stepbloomjoy.com.au<br>P:0400518276<br>www.stepbloomjoy.com.au<br>Riverside/Hillcrest</p>
    <div class="stamp-box"></div>
    <div class="address-line" style="top:210px"></div>
    <div class="address-line" style="top:255px"></div>
    <div class="address-line" style="top:300px"></div>
  </section>
</body>
</html>
```